Digital Ad for mobile charging station

Digital ad for a charging station - specs and example are included in attached document. We often use the "background pattern" (also attached).

Copy:
PUTTING A CREATIVE SPIN ON REIT FINANCING
<QBM LOGO>
<Image of spinning top toy>

Joint Venture - NNN Lease - Mezzanine - Preferred Equity

qbmreit.com

NOTE: The image does NOT have to be a spinning top toy. It could be anything that spins....

```html
<!DOCTYPE html>
<html lang="en">
<head>
<meta charset="utf-8">
<title>QBM REIT – Creative Spin on REIT Financing</title>
<link href="https://fonts.googleapis.com/css2?family=Open+Sans:wght@300;400;600;700;800&display=swap" rel="stylesheet">
<style>
  :root {
    --bg-top: #5a72c4;
    --bg-mid: #4a63b8;
    --bg-bottom: #3b54ad;
    --band: rgba(40, 58, 140, 0.72);
    --white: #ffffff;
    --accent: #5fc6ee;
    --spinner-light: #7fd3f2;
    --spinner-mid: #2f9ad6;
    --spinner-deep: #24408f;
  }
  * { margin: 0; padding: 0; box-sizing: border-box; }
  html, body { width: 1200px; height: 675px; overflow: hidden; }
  body { font-family: "Open Sans", Arial, sans-serif; }

  .ad {
    position: relative;
    width: 1200px;
    height: 675px;
    overflow: hidden;
    background:
      radial-gradient(ellipse at 20% 10%, rgba(140,150,220,0.35), transparent 55%),
      linear-gradient(160deg, var(--bg-top) 0%, var(--bg-mid) 50%, var(--bg-bottom) 100%);
    color: var(--white);
  }

  .services-band {
    position: absolute;
    left: 0; top: 38px;
    width: 100%; height: 63px;
    background: var(--band);
    display: flex; align-items: center; justify-content: center;
  }
  .services-band p {
    font-weight: 700;
    font-size: 28px;
    letter-spacing: 0.02em;
    white-space: nowrap;
  }

  .spinner-visual {
    position: absolute;
    left: 780px; top: 150px;
    width: 420px; height: 410px;
    border-radius: 48% 20% 40% 52% / 46% 30% 50% 50%;
    background:
      radial-gradient(circle at 58% 30%, var(--spinner-light) 0%, transparent 32%),
      radial-gradient(circle at 40% 72%, var(--spinner-mid) 0%, transparent 45%),
      radial-gradient(ellipse at 55% 50%, rgba(47,154,214,0.75) 0%, rgba(36,64,143,0.3) 60%, transparent 75%);
    filter: blur(2px);
  }

  .headline {
    position: absolute;
    left: 60px; top: 192px;
    text-transform: uppercase;
    line-height: 1;
  }
  .headline span { display: block; white-space: nowrap; }
  .headline .light {
    font-weight: 300;
    font-size: 66px;
    letter-spacing: 0.085em;
  }
  .headline .bold {
    font-weight: 700;
    font-size: 70px;
    letter-spacing: 0.1em;
    margin: 20px 0 22px;
  }

  .brand {
    position: absolute;
    left: 64px; top: 500px;
    display: flex; align-items: center; gap: 16px;
  }
  .brand-square {
    width: 30px; height: 30px;
    background: var(--white);
  }
  .brand-name {
    font-weight: 700;
    font-size: 72px;
    letter-spacing: 0.02em;
    line-height: 1;
  }

  .website {
    position: absolute;
    left: 360px; top: 518px;
    font-weight: 600;
    font-size: 68px;
    line-height: 1;
    color: var(--accent);
  }
</style>
</head>
<body>
  <main class="ad">
    <div class="services-band">
      <p>JOINT VENTURE - NNN LEASE - MEZZANINE - PREFERRED EQUITY</p>
    </div>

    <div class="spinner-visual" role="img" aria-label="Photo of a blue fidget spinner with spinning bearings"></div>

    <h1 class="headline">
      <span class="light">Putting a</span>
      <span class="bold">Creative Spin</span>
      <span class="light">on REIT Financing</span>
    </h1>

    <div class="brand">
      <span class="brand-square"></span>
      <span class="brand-name">QBM</span>
    </div>

    <p class="website">qbmreit.com</p>
  </main>
</body>
</html>
```